Website for a Party Bus charter business

Please prepare a site for a local party bus charter company names Fenwick Bus Company.
They hire a party bus, chatrer bus, boat hire and party trailer hire (place holder photos fine for these items).
I have included a wireframe design. This should be used, however creative licence is fully extended
Delivery of PSD is required and all fonts and source files
The client likes: http://www.tallpinoca.com.au/ but must not look completely the same.
Should use a gold (simualr to #D1CFA1) colour, even if just background.
Hi All, just wondering if anyone is working on this as I have not received any responses or questions?
Is there anything I can do to assist?
Thanks all for the great submissions. I will be sending these onto the client today. Will let you know the outcome as soon as I can
Business

```html
<!DOCTYPE html>
<html lang="en">
<head>
<meta charset="utf-8">
<title>Fenwick Bus Company</title>
<link href="https://fonts.googleapis.com/css2?family=Arimo:wght@400;700&family=Open+Sans:wght@400;600&family=Oswald:wght@500&display=swap" rel="stylesheet">
<style>
:root{
  --bg-deep:#16151f;
  --bg-mid:#29283d;
  --gold:#f8c22d;
  --gold-text:#1b1a24;
  --card:#1d1c27;
  --card-line:#393848;
  --text:#ffffff;
  --muted:#a9a8b6;
  --accent-red:#d8262e;
  --field:#ffffff;
  --search-btn:#3c5cb0;
  --rule:#4a4958;
}
*{margin:0;padding:0;box-sizing:border-box}
html,body{width:797px;height:1200px;overflow:hidden}
body{
  position:relative;
  font-family:"Arimo",Arial,sans-serif;
  color:var(--text);
  background:radial-gradient(ellipse at 50% 40%,var(--bg-mid) 0%,var(--bg-deep) 85%);
}
.abs{position:absolute}
/* header */
.brand{left:140px;top:22px;width:112px;text-align:center}
.brand-mark{width:54px;height:54px;border-radius:50%;background:#6e6fb8;margin:0 auto 6px}
.brand-name{font-family:"Arimo",sans-serif;font-weight:700;font-size:17px;line-height:18px;color:var(--text)}
.brand-sub{font-family:"Arimo",sans-serif;font-weight:700;font-size:17px;letter-spacing:3px;line-height:18px;color:var(--text)}
.connect{right:118px;top:10px;display:flex;align-items:center;gap:6px;font-size:7.5px;color:#d9d8e3}
.connect svg{margin-right:10px}
.social{display:flex;gap:5px}
.social span{display:block;width:10px;height:10px;border-radius:2px}
.s1{background:var(--accent-red)}.s2{background:#2aa3d8}.s3{background:#3d5fa8}
.connect .social{position:absolute;left:100%;margin-left:8px}
.phone{right:118px;top:24px;font-family:"Open Sans",serif;font-size:20px;color:var(--text)}
.like-badge{left:490px;top:57px;width:38px;height:10px;background:#fff;border-radius:1px}
.like-badge::before{content:"";position:absolute;left:0;top:0;width:24px;height:10px;background:#4a66a0}
.search{left:537px;top:54px;width:142px;height:17px;display:flex}
.search input{flex:1;border:0;background:var(--field);font:8px "Arimo",sans-serif;padding-left:6px;color:#555}
.search button{width:21px;border:0;background:var(--search-btn);display:flex;align-items:center;justify-content:center}
.nav{left:293px;top:79px;width:388px;height:27px;background:var(--gold);display:flex;align-items:center;justify-content:center;font-size:9.5px;color:var(--gold-text)}
.nav a{color:inherit;text-decoration:none;padding:0 8px;border-left:1px solid var(--gold-text);line-height:10px}
.nav a:first-child{border-left:0}
/* hero */
.hero{left:121px;top:116px;width:560px;height:244px;border:4px solid #fff;background:linear-gradient(110deg,#2c3170 0%,#4a3b7a 35%,#7b5a5c 60%,#3a2a3a 100%)}
.hero-title{left:38px;top:128px;font-family:"Oswald",sans-serif;font-size:32px;letter-spacing:0.5px;color:#fff}
.hero-tag{left:38px;top:168px;font-family:"Open Sans",sans-serif;font-size:29px;color:#fff}
.dots{right:12px;bottom:8px;display:flex;gap:4px}
.dots span{width:7px;height:7px;border-radius:50%;background:#fff}
/* welcome */
h2{font-family:"Arimo",sans-serif;font-weight:400;font-size:20px;color:var(--text)}
.welcome-h{left:121px;top:380px}
.welcome-p{left:121px;top:413px;width:367px;font-size:8.6px;line-height:12.6px;color:var(--muted)}
.fb-box{left:510px;top:385px;width:170px;height:100px;background:#fff;color:#333;font-size:6px;padding:7px}
.fb-head{display:flex;gap:6px;align-items:flex-start}
.fb-avatar{width:20px;height:14px;border-radius:50%;background:#6e6fb8}
.fb-name{color:#3b5998;font-size:6.5px}
.fb-btn{display:block;width:22px;height:9px;background:#4a66a0;margin-top:4px}
.fb-line{border-top:1px solid #ddd;margin:8px 0 4px}
.fb-faces{display:flex;gap:3px;margin-top:5px}
.fb-faces span{width:23px;height:22px;background:linear-gradient(#c99a7c,#7c5a54)}
.fb-foot{border-top:1px solid #ddd;margin-top:6px;padding-top:4px;color:#888;font-size:5px}
/* services */
.services-h{left:121px;top:494px}
.btn{background:var(--gold);color:var(--gold-text);font-family:"Arimo",sans-serif;display:flex;align-items:center;justify-content:center}
.view-all{left:616px;top:500px;width:63px;height:18px;font-size:12px}
.card{width:267px;height:92px;background:var(--card);border:1px solid var(--card-line)}
.card-img{position:absolute;left:14px;top:13px;width:107px;height:66px}
.card h3{position:absolute;left:131px;top:12px;font-family:"Open Sans",sans-serif;font-weight:400;font-size:12px}
.card p{position:absolute;left:131px;top:33px;width:126px;font-size:7.4px;line-height:11px;color:var(--muted)}
.more{color:var(--accent-red)}
/* coast */
.coast-h{left:121px;top:750px}
.coast-img{left:121px;top:787px;width:278px;height:140px;border:4px solid #fff;background:linear-gradient(160deg,#6aa3d6 0%,#b98a6e 55%,#5c4a48 100%)}
.coast-p{left:409px;top:789px;width:272px;font-size:8.6px;line-height:12.5px;color:var(--muted)}
.book{left:564px;top:893px;width:114px;height:28px;font-size:17px}
.rule{left:121px;width:560px;height:1px;background:var(--rule)}
/* footer columns */
.col-h{top:962px;font-size:16px}
.col-p{font-size:7.4px;line-height:11px;color:var(--muted)}
.quote{left:121px;top:1051px;width:115px;height:28px;font-size:17px}
.post{left:337px;width:170px;height:45px}
.post .thumb{position:absolute;left:0;top:0;width:51px;height:44px;background:linear-gradient(135deg,#c99a7c,#4c3a40)}
.post h4{position:absolute;left:59px;top:2px;font-size:8px;font-weight:700}
.post p{position:absolute;left:59px;top:13px;width:112px}
.field{left:542px;width:138px;height:16px;background:var(--field);color:#333;font-size:7.5px;padding:4px 8px}
.join{left:542px;top:1077px;width:62px;height:17px;font-size:11px}
.copy{left:121px;top:1124px;font-size:7.2px;color:var(--muted)}
.privacy{left:121px;top:1137px;font-size:7.2px;color:var(--muted);text-decoration:underline}
.foot-social{left:636px;top:1131px}
</style>
</head>
<body>
<header>
  <div class="abs brand">
    <div class="brand-mark"></div>
    <div class="brand-name">Fenwick Bus</div>
    <div class="brand-sub">COMPANY</div>
  </div>
  <div class="abs connect" style="right:168px">
    <svg width="11" height="10" viewBox="0 0 11 10"><path d="M5.5 0 L11 5 H9 V10 H6.5 V7 H4.5 V10 H2 V5 H0 Z" fill="#fff"/></svg>
    <span>Connect with us!</span>
  </div>
  <div class="abs social" style="left:638px;top:10px"><span class="s1"></span><span class="s2"></span><span class="s3"></span></div>
  <div class="abs phone">123 456 7890</div>
  <div class="abs like-badge"></div>
  <form class="abs search">
    <input type="text" placeholder="Enter Keyword here">
    <button type="button" aria-label="Search"><svg width="9" height="9" viewBox="0 0 9 9"><circle cx="3.5" cy="3.5" r="2.5" stroke="#fff" stroke-width="1.3" fill="none"/><path d="M5.5 5.5 L8.5 8.5" stroke="#fff" stroke-width="1.5"/></svg></button>
  </form>
  <nav class="abs nav">
    <a href="#">Party Bus</a><a href="#">Charter Bus</a><a href="#">Party Trailer</a><a href="#">Party Boat</a><a href="#">House Bus</a><a href="#">Want you own?</a>
  </nav>
</header>

<section class="abs hero" role="img" aria-label="Guests celebrating inside a neon-lit party bus">
  <div class="abs hero-title">FENWICK BUS</div>
  <div class="abs hero-tag">Ultimate Party Experience!</div>
  <div class="abs dots"><span></span><span></span><span></span></div>
</section>

<h2 class="abs welcome-h">Welcome to Fenwick Bus Company</h2>
<p class="abs welcome-p">Our staff of highly skilled drivers provide our passengers with professional service of unmatched luxury and quality. We take great pride in providing the very best in high quality affodable luxury transportation.This enables us to operate our party bus and limousine services with absolute confi-dence and pride. As a leading party bus and limo rental company we can provide you with a wide range of transportation services.</p>

<aside class="abs fb-box">
  <div class="fb-head"><div class="fb-avatar"></div><div><div class="fb-name">Fenwick Bus</div><span class="fb-btn"></span></div></div>
  <div class="fb-line"></div>
  <div>9,890 people like <span class="fb-name">Fenwick Bus</span></div>
  <div class="fb-faces"><span></span><span></span><span></span><span></span><span></span><span></span></div>
  <div class="fb-foot">Social plugin</div>
</aside>

<h2 class="abs services-h">Our Services</h2>
<div class="abs btn view-all">View All</div>

<article class="abs card" style="left:121px;top:533px">
  <div class="card-img" role="img" aria-label="White party bus" style="background:linear-gradient(135deg,#4a5e8a,#d8d8e0 55%,#2b2b35)"></div>
  <h3>Party Bus</h3>
  <p>Lorem ipsum dolor sit amet, con-sectetur adipiscing elit. Curabitur venenatis <span class="more">more..</span></p>
</article>
<article class="abs card" style="left:413px;top:533px">
  <div class="card-img" role="img" aria-label="Charter bus interior with seats" style="background:linear-gradient(135deg,#d9dde6,#5a6aa8 60%,#2f3a6a)"></div>
  <h3>Charter Bus</h3>
  <p>Lorem ipsum dolor sit amet, con-sectetur adipiscing elit. Curabitur venenatis <span class="more">more..</span></p>
</article>
<article class="abs card" style="left:121px;top:638px">
  <div class="card-img" role="img" aria-label="Party trailer lit at night" style="background:linear-gradient(135deg,#1e2a48,#6a5a6e 55%,#20202a)"></div>
  <h3>Party Trailer</h3>
  <p>&nbsp; orem ipsum dolor sit amet, con-sectetur adipiscing elit. Curabitur venenatis vehicula vitae <span class="more">more..</span></p>
</article>
<article class="abs card" style="left:413px;top:638px">
  <div class="card-img" role="img" aria-label="Party boat on the water" style="background:linear-gradient(180deg,#6a9ad0,#e0e4ea 50%,#2f8a9a)"></div>
  <h3>Party Boat</h3>
  <p>Lorem ipsum dolor sit amet, con-sectetur adipiscing elit. Curabitur venenatis <span class="more">more..</span></p>
</article>

<h2 class="abs coast-h">Best Way To See The Coast</h2>
<div class="abs coast-img" role="img" aria-label="Group of friends celebrating on a boat"></div>
<p class="abs coast-p">Lorem ipsum dolor sit amet, consectetur adipiscing elit. Curabitur ven-enatis vehicula tellus, id mattis neque accumsan vitae. Fusce rhoncus erat in ullamcorper rutrum. Nam aliquam non neque eu rhoncus. Etiam euismod sed est quis porta. Aliquam erat volutpat. Aliquam erat volutpat. Donec lacinia, erat vel placerat tincidunt, erat libero pharetra erat, ac luctus enim tortor ac eros.</p>
<div class="abs btn book">Book It Now</div>

<div class="abs rule" style="top:945px"></div>

<footer>
  <h2 class="abs col-h" style="left:121px">Quotes &amp; Bookings</h2>
  <p class="abs col-p" style="left:121px;top:990px;width:180px">Lorem ipsum dolor sit amet, consectetur adipiscing elit. Curabitur venenatis vehicula tellus, id mattis neque accumsan vitae. Fusce rhoncus erat in ullamcorper rutrum. Nam aliquam non neque eu rhoncus.</p>
  <div class="abs btn quote">Get A Quote</div>

  <h2 class="abs col-h" style="left:337px">Latest Blog Poste</h2>
  <div class="abs post" style="top:990px">
    <div class="thumb" role="img" aria-label="Blog post photo of friends partying"></div>
    <h4>Lorem ipsum dolor sit amet</h4>
    <p class="col-p">Consectetur adipiscing elit. Curabi-tur venenatis vehicula tellus, id</p>
  </div>
  <div class="abs post" style="top:1051px">
    <div class="thumb" role="img" aria-label="Blog post photo of friends partying"></div>
    <h4>Lorem ipsum dolor sit amet</h4>
    <p class="col-p">Consectetur adipiscing elit. Curabi-tur venenatis vehicula tellus, id</p>
  </div>

  <h2 class="abs col-h" style="left:542px">Join Our VIP Club</h2>
  <p class="abs col-p" style="left:542px;top:990px;width:140px">Lorem ipsum dolor sit amet, consectetur adipiscing elit.</p>
  <div class="abs field" style="top:1022px">Your Name</div>
  <div class="abs field" style="top:1049px">Email Address</div>
  <div class="abs btn join">Join Now</div>

  <div class="abs rule" style="top:1114px"></div>
  <div class="abs copy">Copyright 2014 Fenwick Party company. All Rights Reserved.</div>
  <div class="abs privacy">Privacy Policy</div>
  <div class="abs social foot-social"><span class="s1"></span><span class="s2"></span><span class="s3"></span></div>
</footer>
</body>
</html>
```